WPF Application Design

I require a design for a WPF application. I have the screenshots which needs to be redesigned for WPF application. Screens have different standard controls used, designer should suggest best placement and styling for the screens.

```html
<!DOCTYPE html>
<html lang="en">
<head>
<meta charset="utf-8">
<title>StepFlow – Course Templete Manager</title>
<link rel="stylesheet" href="https://fonts.googleapis.com/css2?family=Oswald:wght@300;400;500&family=Roboto:wght@400;700&display=swap">
<style>
:root{
  --cyan:#02a9df;
  --cyan-light:#1ab4e6;
  --ink:#1d5d80;
  --ink-dark:#174e6d;
  --panel:#1a1a1a;
  --cell:#1e1e1e;
  --cell-line:#3a3a3a;
  --black:#0d0d0d;
  --white:#ffffff;
  --chrome:#c3c3c3;
  --online:#2fd14a;
  --search:#0b6e95;
}
*{box-sizing:border-box;margin:0;padding:0}
html,body{width:1200px;height:678px;overflow:hidden;background:var(--black)}
.app{position:absolute;left:0;top:0;width:1360px;height:768px;transform:scale(.88235,.88281);transform-origin:0 0;font-family:"Oswald",sans-serif;background:var(--black);overflow:hidden}

/* window chrome */
.titlebar{position:absolute;left:0;top:0;width:1360px;height:27px;background:var(--chrome);display:flex;align-items:center;justify-content:center;font:700 13px "Roboto",sans-serif;color:#222}
.window-controls{position:absolute;right:8px;top:6px;display:flex;gap:8px}

/* top navigation */
.topnav{position:absolute;left:0;top:27px;width:1360px;height:50px;background:var(--cyan);border-bottom:1px solid var(--black)}
.avatar{position:absolute;left:170px;top:9px}
.nav-links{position:absolute;left:271px;top:0;height:50px;display:flex;list-style:none}
.nav-links li{height:50px;line-height:49px;font-size:13px;color:var(--ink);margin-right:19px;letter-spacing:.2px}
.nav-links li.is-active{font-weight:500;color:#1b4660;border-bottom:2px solid #2a3f4c;margin-right:18px}
.search{position:absolute;left:929px;top:15px;width:142px;height:20px;background:var(--search);color:#cfe8f3;font:400 12px "Roboto",sans-serif;padding:3px 8px}
.nav-icon{position:absolute;top:13px}

/* hierarchy tree */
.tree-panel{position:absolute;left:0;top:78px;width:330px;height:690px;background:var(--cyan)}
.tree-title{height:60px;border-bottom:1px solid #1b3a4c;font-weight:300;font-size:24px;color:var(--ink);text-align:center;line-height:60px;letter-spacing:.3px}
.tree{list-style:none;position:absolute;top:74px;left:0;width:330px}
.tree li{position:relative;height:32px;display:flex;align-items:center;font-size:14px;color:var(--ink)}
.tree li.gap{margin-top:5px}
.tree .caret{position:absolute;width:0;height:0;border-left:4px solid transparent;border-right:4px solid transparent;border-top:5px solid var(--ink-dark);transform:rotate(45deg)}
.tree svg{position:absolute}
.lvl0 svg{left:40px}.lvl0 span{margin-left:85px}.lvl0 .caret{left:23px}
.lvl1 svg{left:71px}.lvl1 span{margin-left:115px}
.lvl2 svg{left:101px}.lvl2 span{margin-left:145px}.lvl2 .caret{left:83px}
.lvl3 svg{left:131px}.lvl3 span{margin-left:175px}
.scrollbar{position:absolute;left:330px;top:78px;width:15px;height:690px;background:#d9eef6}
.scroll-thumb{position:absolute;left:1px;top:14px;width:13px;height:452px;background:var(--white)}
.scroll-arrow{position:absolute;left:3px;width:0;height:0;border-left:4px solid transparent;border-right:4px solid transparent}

/* main area */
.panel{position:absolute;left:347px;width:1011px;border:1px solid #e6e6e6;background:var(--panel)}
.header-panel{top:78px;height:59px;display:flex;align-items:center;justify-content:center;font-weight:500;font-size:18px;letter-spacing:3.4px;color:var(--white)}
.grid-panel{top:139px;height:310px}
.grid{position:absolute;left:3px;top:5px;display:grid;grid-template-columns:repeat(6,166px);column-gap:2px}
.grid .th{height:30px;background:var(--cyan);color:var(--ink);font-size:12px;padding:6px 8px;position:relative;margin-bottom:7px}
.grid .th svg{position:absolute;right:7px;top:12px}
.grid .td{height:31px;background:var(--cell);border:1px solid var(--cell-line);color:var(--white);font:400 14px "Roboto",sans-serif;padding:8px 8px;margin-bottom:0}

.detail-panel{top:452px;height:308px}
.tabs{position:absolute;left:5px;top:8px;display:flex;gap:3px}
.tab{width:139px;height:31px;background:var(--cyan);color:var(--ink);font-size:12px;padding:7px 8px}
.tab.is-active{background:var(--panel);color:var(--white);border:1px solid #e6e6e6;border-bottom:none;height:36px;width:141px;margin:0 2px}
.group{position:absolute;top:44px;height:253px;border:1px solid #e6e6e6;background:var(--panel);color:var(--white)}
.price-group{left:5px;width:498px}
.discount-group{left:509px;width:498px}
.group h2{position:absolute;top:12px;font-weight:400;font-size:20px}
.price-group h2{left:16px}
.discount-group h2{left:17px}
.caption{position:absolute;font-size:12px;font-weight:500}
.field-row{position:absolute;left:0;width:496px;height:22px;font-size:12px}
.field-row > *{position:absolute;top:0}
.input{height:22px;border:1px solid #e6e6e6;background:var(--panel);color:var(--white);font:400 12px "Oswald",sans-serif;padding:3px 4px}
.label{line-height:22px;font-weight:500}
.radio{width:14px;height:14px;border-radius:50%;background:var(--white);top:4px!important}
.radio.on::after{content:"";position:absolute;left:4px;top:4px;width:6px;height:6px;border-radius:50%;background:var(--cyan)}
.check{width:14px;height:14px;background:var(--white);top:4px!important}
.check svg{position:absolute;left:1px;top:1px}
</style>
</head>
<body>
<div class="app">

  <header class="titlebar">StepFlow
    <div class="window-controls">
      <svg width="12" height="12" viewBox="0 0 12 12"><rect x="1" y="8" width="9" height="2" fill="#222"/></svg>
      <svg width="12" height="12" viewBox="0 0 12 12"><rect x="1.5" y="1.5" width="9" height="8" fill="none" stroke="#222" stroke-width="1.5"/><rect x="1.5" y="1.5" width="9" height="2" fill="#222"/></svg>
      <svg width="12" height="12" viewBox="0 0 12 12"><path d="M2 2l8 8M10 2l-8 8" stroke="#222" stroke-width="2"/></svg>
    </div>
  </header>

  <nav class="topnav">
    <svg class="avatar" width="42" height="34" viewBox="0 0 42 34" aria-label="User">
      <circle cx="16" cy="16" r="15" fill="var(--ink)"/>
      <circle cx="16" cy="12" r="6" fill="var(--cyan)"/>
      <path d="M5 26c3-6 7-8 11-8s8 2 11 8" fill="var(--cyan)"/>
      <circle cx="35" cy="27" r="5" fill="var(--online)"/>
    </svg>
    <ul class="nav-links">
      <li class="is-active">Home</li>
      <li>Course Hierarchy Manager</li>
      <li>Crouse Group</li>
      <li>Course Type</li>
      <li>Course Step</li>
      <li>Course Templete</li>
    </ul>
    <div class="search">search</div>
    <svg class="nav-icon" style="left:1100px" width="20" height="20" viewBox="0 0 20 20" aria-label="Settings">
      <g fill="var(--ink)"><circle cx="10" cy="10" r="6.5"/><rect x="8.3" y="1" width="3.4" height="18" rx="1"/><rect x="8.3" y="1" width="3.4" height="18" rx="1" transform="rotate(60 10 10)"/><rect x="8.3" y="1" width="3.4" height="18" rx="1" transform="rotate(120 10 10)"/></g>
      <circle cx="10" cy="10" r="2.8" fill="var(--cyan)"/>
    </svg>
    <svg class="nav-icon" style="left:1145px" width="20" height="20" viewBox="0 0 20 20" aria-label="Power">
      <path d="M6 4.5a7 7 0 1 0 8 0" fill="none" stroke="var(--ink)" stroke-width="2.4" stroke-linecap="round"/>
      <path d="M10 1.5v8" stroke="var(--ink)" stroke-width="2.4" stroke-linecap="round"/>
    </svg>
  </nav>

  <aside class="tree-panel">
    <div class="tree-title">COURSE HIERARCHY TREE</div>
    <ul class="tree">
      <li class="lvl0"><i class="caret"></i><svg width="28" height="18" viewBox="0 0 28 18"><path d="M0 2h11l2 2h15v14H0z" fill="var(--ink-dark)"/></svg><span>All Course Group</span></li>
      <li class="lvl1"><svg width="28" height="18" viewBox="0 0 28 18"><path d="M0 2h11l2 2h15v14H0z" fill="var(--ink-dark)"/></svg><span>Course Group 1</span></li>
      <li class="lvl1"><svg width="28" height="18" viewBox="0 0 28 18"><path d="M0 2h11l2 2h15v14H0z" fill="var(--ink-dark)"/></svg><span>Course Group 2</span></li>
      <li class="lvl1"><svg width="28" height="18" viewBox="0 0 28 18"><path d="M0 2h11l2 2h15v14H0z" fill="var(--ink-dark)"/></svg><span>Course Group 3</span></li>
      <li class="lvl1"><i class="caret" style="left:53px"></i><svg width="28" height="18" viewBox="0 0 28 18"><path d="M0 2h11l2 2h15v14H0z" fill="var(--ink-dark)"/></svg><span>Course Group 4</span></li>
      <li class="lvl2"><i class="caret"></i><svg width="28" height="18" viewBox="0 0 28 18"><path d="M0 2h11l2 2h15v14H0z" fill="var(--ink-dark)"/></svg><span>Title</span></li>
      <li class="lvl3"><svg width="28" height="18" viewBox="0 0 28 18"><path d="M0 2h11l2 2h15v14H0z" fill="var(--ink-dark)"/></svg><span>Title</span></li>
      <li class="lvl3"><svg width="28" height="18" viewBox="0 0 28 18"><path d="M0 2h11l2 2h15v14H0z" fill="var(--ink-dark)"/></svg><span>Title</span></li>
      <li class="lvl2"><i class="caret"></i><svg width="28" height="18" viewBox="0 0 28 18"><path d="M0 2h11l2 2h15v14H0z" fill="var(--ink-dark)"/></svg><span>Title</span></li>
      <li class="lvl3"><svg width="28" height="18" viewBox="0 0 28 18"><path d="M0 2h11l2 2h15v14H0z" fill="var(--ink-dark)"/></svg><span>Title</span></li>
      <li class="lvl3"><svg width="28" height="18" viewBox="0 0 28 18"><path d="M0 2h11l2 2h15v14H0z" fill="var(--ink-dark)"/></svg><span>Title</span></li>
      <li class="lvl1 gap"><svg width="28" height="18" viewBox="0 0 28 18"><path d="M0 2h11l2 2h15v14H0z" fill="var(--ink-dark)"/></svg><span>Course Group 5</span></li>
      <li class="lvl1"><svg width="28" height="18" viewBox="0 0 28 18"><path d="M0 2h11l2 2h15v14H0z" fill="var(--ink-dark)"/></svg><span>Course Group 6</span></li>
      <li class="lvl1"><svg width="28" height="18" viewBox="0 0 28 18"><path d="M0 2h11l2 2h15v14H0z" fill="var(--ink-dark)"/></svg><span>Course Group 7</span></li>
      <li class="lvl1"><svg width="28" height="18" viewBox="0 0 28 18"><path d="M0 2h11l2 2h15v14H0z" fill="var(--ink-dark)"/></svg><span>Course Group 8</span></li>
      <li class="lvl1"><svg width="28" height="18" viewBox="0 0 28 18"><path d="M0 2h11l2 2h15v14H0z" fill="var(--ink-dark)"/></svg><span>Course Group 9</span></li>
      <li class="lvl1"><svg width="28" height="18" viewBox="0 0 28 18"><path d="M0 2h11l2 2h15v14H0z" fill="var(--ink-dark)"/></svg><span>Course Group 10</span></li>
      <li class="lvl1"><svg width="28" height="18" viewBox="0 0 28 18"><path d="M0 2h11l2 2h15v14H0z" fill="var(--ink-dark)"/></svg><span>Course Group 11</span></li>
      <li class="lvl1"><svg width="28" height="18" viewBox="0 0 28 18"><path d="M0 2h11l2 2h15v14H0z" fill="var(--ink-dark)"/></svg><span>Course Group 12</span></li>
    </ul>
  </aside>
  <div class="scrollbar">
    <i class="scroll-arrow" style="top:4px;border-bottom:5px solid #6a8a99"></i>
    <div class="scroll-thumb"></div>
    <i class="scroll-arrow" style="bottom:8px;border-top:5px solid #6a8a99"></i>
  </div>

  <section class="panel header-panel">COURSE TEMPLETE MANAGER</section>

  <section class="panel grid-panel">
    <div class="grid">
      <div class="th">Templete Number<svg width="9" height="8" viewBox="0 0 9 8"><path d="M0 0h9L5.5 4v4h-2V4z" fill="var(--ink)"/></svg></div>
      <div class="th">Templete Name<svg width="9" height="8" viewBox="0 0 9 8"><path d="M0 0h9L5.5 4v4h-2V4z" fill="var(--ink)"/></svg></div>
      <div class="th">Number of Lessons<svg width="9" height="8" viewBox="0 0 9 8"><path d="M0 0h9L5.5 4v4h-2V4z" fill="var(--ink)"/></svg></div>
      <div class="th">Lesson Duration (min)<svg width="9" height="8" viewBox="0 0 9 8"><path d="M0 0h9L5.5 4v4h-2V4z" fill="var(--ink)"/></svg></div>
      <div class="th">Created Date<svg width="9" height="8" viewBox="0 0 9 8"><path d="M0 0h9L5.5 4v4h-2V4z" fill="var(--ink)"/></svg></div>
      <div class="th">Modified Date<svg width="9" height="8" viewBox="0 0 9 8"><path d="M0 0h9L5.5 4v4h-2V4z" fill="var(--ink)"/></svg></div>
      <div class="td">0000</div><div class="td">0000</div><div class="td">0000</div><div class="td">0000</div><div class="td">0000</div><div class="td">0000</div>
      <div class="td"></div><div class="td"></div><div class="td"></div><div class="td"></div><div class="td"></div><div class="td"></div>
      <div class="td"></div><div class="td"></div><div class="td"></div><div class="td"></div><div class="td"></div><div class="td"></div>
      <div class="td"></div><div class="td"></div><div class="td"></div><div class="td"></div><div class="td"></div><div class="td"></div>
    </div>
  </section>

  <section class="panel detail-panel">
    <div class="tabs">
      <div class="tab">Templete Type</div>
      <div class="tab">General</div>
      <div class="tab is-active">Financial</div>
      <div class="tab">Preliminary Course</div>
      <div class="tab">Package</div>
      <div class="tab">Learning Goals</div>
      <div class="tab">Remarks</div>
    </div>

    <div class="group price-group">
      <h2>Price &amp; Payment</h2>
      <span class="caption" style="left:411px;top:26px">Changeable</span>
      <span class="caption" style="left:411px;top:52px">Yes</span>
      <span class="caption" style="left:457px;top:52px">No</span>
      <span class="caption" style="left:319px;top:55px">Discount Point</span>

      <div class="field-row" style="top:78px">
        <i class="check" style="left:14px"><svg width="12" height="12" viewBox="0 0 12 12"><path d="M2 6l3 3 6-8" fill="none" stroke="var(--cyan)" stroke-width="2"/></svg></i>
        <span class="input" style="left:36px;width:61px">1.00</span>
        <span class="label" style="left:107px">CHF fixed price per course</span>
        <span class="input" style="left:325px;width:62px">4.00</span>
        <i class="radio on" style="left:413px"></i><i class="radio" style="left:457px"></i>
      </div>
      <div class="field-row" style="top:105px">
        <i class="check" style="left:14px"><svg width="12" height="12" viewBox="0 0 12 12"><path d="M2 6l3 3 6-8" fill="none" stroke="var(--cyan)" stroke-width="2"/></svg></i>
        <span class="input" style="left:36px;width:61px">2.00</span>
        <span class="label" style="left:107px">CHF - Small class charge</span>
        <span class="input" style="left:325px;width:62px">4.00</span>
        <i class="radio on" style="left:413px"></i><i class="radio" style="left:457px"></i>
      </div>
      <div class="field-row" style="top:133px">
        <i class="check" style="left:14px"><svg width="12" height="12" viewBox="0 0 12 12"><path d="M2 6l3 3 6-8" fill="none" stroke="var(--cyan)" stroke-width="2"/></svg></i>
        <span class="input" style="left:36px;width:61px">3.00</span>
        <span class="label" style="left:107px">CHF individual acceptance in courses</span>
        <span class="input" style="left:325px;width:62px">4.00</span>
        <i class="radio on" style="left:413px"></i><i class="radio" style="left:457px"></i>
      </div>
    </div>

    <div class="group discount-group">
      <h2>Discount</h2>
      <span class="caption" style="left:273px;top:26px">Discount In</span>
      <span class="caption" style="left:416px;top:26px">Changeable</span>
      <span class="caption" style="left:416px;top:52px">Yes</span>
      <span class="caption" style="left:461px;top:52px">No</span>

      <div class="field-row" style="top:75px"><span class="label" style="left:16px">Few Discount</span><span class="input" style="left:203px;width:61px">4.00</span><i class="radio on" style="left:271px"></i><span class="label" style="left:290px">%</span><i class="radio" style="left:315px"></i><span class="label" style="left:335px">Actual</span><i class="check" style="left:376px"><svg width="12" height="12" viewBox="0 0 12 12"><path d="M2 6l3 3 6-8" fill="none" stroke="var(--cyan)" stroke-width="2"/></svg></i><i class="radio on" style="left:418px"></i><i class="radio" style="left:461px"></i></div>
      <div class="field-row" style="top:104px"><span class="label" style="left:16px">Follow Up Course Discount</span><span class="input" style="left:203px;width:61px">4.00</span><i class="radio on" style="left:271px"></i><span class="label" style="left:290px">%</span><i class="radio" style="left:315px"></i><span class="label" style="left:335px">Actual</span><i class="check" style="left:376px"><svg width="12" height="12" viewBox="0 0 12 12"><path d="M2 6l3 3 6-8" fill="none" stroke="var(--cyan)" stroke-width="2"/></svg></i><i class="radio on" style="left:418px"></i><i class="radio" style="left:461px"></i></div>
      <div class="field-row" style="top:133px"><span class="label" style="left:16px">Direct Follow Up Course Discount</span><span class="input" style="left:203px;width:61px">4.00</span><i class="radio on" style="left:271px"></i><span class="label" style="left:290px">%</span><i class="radio" style="left:315px"></i><span class="label" style="left:335px">Actual</span><i class="check" style="left:376px"><svg width="12" height="12" viewBox="0 0 12 12"><path d="M2 6l3 3 6-8" fill="none" stroke="var(--cyan)" stroke-width="2"/></svg></i><i class="radio on" style="left:418px"></i><i class="radio" style="left:461px"></i></div>
      <div class="field-row" style="top:162px"><span class="label" style="left:16px">Total Packet Discount</span><span class="input" style="left:203px;width:61px">4.00</span><i class="radio on" style="left:271px"></i><span class="label" style="left:290px">%</span><i class="radio" style="left:315px"></i><span class="label" style="left:335px">Actual</span><i class="check" style="left:376px"><svg width="12" height="12" viewBox="0 0 12 12"><path d="M2 6l3 3 6-8" fill="none" stroke="var(--cyan)" stroke-width="2"/></svg></i><i class="radio on" style="left:418px"></i><i class="radio" style="left:461px"></i></div>
      <div class="field-row" style="top:191px"><span class="label" style="left:16px">Schooler/Student Discount</span><span class="input" style="left:203px;width:61px">4.00</span><i class="radio on" style="left:271px"></i><span class="label" style="left:290px">%</span><i class="radio" style="left:315px"></i><span class="label" style="left:335px">Actual</span><i class="check" style="left:376px"><svg width="12" height="12" viewBox="0 0 12 12"><path d="M2 6l3 3 6-8" fill="none" stroke="var(--cyan)" stroke-width="2"/></svg></i><i class="radio on" style="left:418px"></i><i class="radio" style="left:461px"></i></div>
      <div class="field-row" style="top:220px"><span class="label" style="left:16px">VIP Discount</span><span class="input" style="left:203px;width:61px">4.00</span><i class="radio on" style="left:271px"></i><span class="label" style="left:290px">%</span><i class="radio" style="left:315px"></i><span class="label" style="left:335px">Actual</span><i class="check" style="left:376px"><svg width="12" height="12" viewBox="0 0 12 12"><path d="M2 6l3 3 6-8" fill="none" stroke="var(--cyan)" stroke-width="2"/></svg></i><i class="radio on" style="left:418px"></i><i class="radio" style="left:461px"></i></div>
    </div>
  </section>

</div>
</body>
</html>
```